business card for LWR pty ltd

We require a business card that stands out . I have included our company flyer and would like the services listed to be put on the card so when we Give out the cards to customers they have an idea of services we provide. need the winning design to be in editable photo shop format, editable iMac pages format or editable windows publisher format, so that I can enter in names, email addresses, phone numbers etc myself. I have included a pdf documents of info / items needed on the card to use as reference please.
Updates

need more submissions

Need extra days to review

Sick

Target Market(s)

new customers

Contact Information for Business Card

details are on attached business card requirements file

Requirements
Must have
• I have attached a list of must haves

```html
<!DOCTYPE html>
<html lang="en">
<head>
<meta charset="utf-8">
<title>LWR pty ltd — Business Card</title>
<link rel="stylesheet" href="https://fonts.googleapis.com/css2?family=Arimo:wght@400;700&display=swap">
<style>
  :root {
    --bg: #e9e7e4;
    --card-white: #fbf8f7;
    --ink: #151515;
    --bar: #0b0b0b;
    --night: #050505;
    --steel: #2a2c30;
    --dust: #a86a4c;
    --dust-light: #c98e70;
    --silver: #b9bcc1;
  }
  * { box-sizing: border-box; margin: 0; padding: 0; }
  html, body {
    width: 1200px; height: 800px; overflow: hidden;
    background: var(--bg);
    font-family: "Arimo", Arial, sans-serif;
    color: var(--ink);
  }
  .canvas {
    position: relative; width: 1200px; height: 800px;
    display: flex; align-items: center; justify-content: center; gap: 60px;
  }
  .card {
    position: relative; width: 520px; height: 298px; overflow: hidden;
    box-shadow: 0 6px 18px rgba(0,0,0,0.18);
  }
  /* Front */
  .card-front { background: var(--card-white); }
  .accent-bar {
    position: absolute; left: 0; top: 118px; width: 20px; height: 92px;
    background: var(--bar);
  }
  .person {
    position: absolute; left: 150px; top: 46px;
    font-size: 24px; letter-spacing: 0.2px;
  }
  .person .role { font-size: 12px; letter-spacing: 1px; margin-left: 4px; }
  .company {
    position: absolute; left: 46px; top: 170px;
    font-size: 14px; line-height: 1.45;
  }
  .contact {
    position: absolute; right: 36px; top: 160px; text-align: right;
    font-size: 14px; line-height: 1.5;
  }
  .contact .phone {
    font-weight: 700; font-size: 22px; letter-spacing: 4px; margin-bottom: 4px;
  }
  /* Back */
  .card-back { background: var(--night); }
  .scene {
    position: absolute; inset: 0; width: 100%; height: 100%;
  }
  .brand-name {
    position: absolute; right: 34px; top: 96px;
    font-size: 76px; font-weight: 700; letter-spacing: 6px;
    color: var(--silver);
  }
</style>
</head>
<body>
<main class="canvas">
  <section class="card card-front" aria-label="Business card front">
    <div class="accent-bar"></div>
    <p class="person">Daniel Harlow <span class="role">Director</span></p>
    <div class="company">
      <p>LWR pty ltd</p>
      <p>Lot 444 example address Australia</p>
    </div>
    <div class="contact">
      <p class="phone">000 444 000</p>
      <p>email@lwrservices.com.au</p>
      <p>www.websiteaddress.com</p>
    </div>
  </section>

  <section class="card card-back" aria-label="Business card back">
    <svg class="scene" viewBox="0 0 520 298" role="img" aria-label="Photograph of a road train truck with tipper trailers on red outback dirt, against a dark metallic mesh background">
      <defs>
        <linearGradient id="sky" x1="0" y1="0" x2="1" y2="0.3">
          <stop offset="0" stop-color="#050505"/>
          <stop offset="0.6" stop-color="#1c1e22"/>
          <stop offset="1" stop-color="#2a2c30"/>
        </linearGradient>
        <linearGradient id="ground" x1="0" y1="0" x2="0" y2="1">
          <stop offset="0" stop-color="#8f5a40"/>
          <stop offset="1" stop-color="#c98e70"/>
        </linearGradient>
      </defs>
      <rect width="520" height="298" fill="url(#sky)"/>
      <polygon points="0,150 390,230 430,298 0,298" fill="url(#ground)"/>
    </svg>
    <p class="brand-name">LWR</p>
  </section>
</main>
</body>
</html>
```